Custom Clothing Store Website/Logo Design

We need a website and Logo design for our company called "quillbarn7823". We will be designing generic and mainly custom made clothing (t shirts, sweaters, hoodies, hats, caps, leggings etc) with other products of electronics and every day products with side sells. We want a catchy but easy to navigate website to use on our SHOPIFY website.
Updates

Designs look the same

Target Market(s)

Anyone that is interested in purchasing custom design clothing.

Logo Text

QuillBarn23'

Number of Pages Required

1 page

Other font styles liked:
• Microbrew

Colors

Designer to choose colors to be used in the design.

```html
<!DOCTYPE html>
<html lang="en">
<head>
<meta charset="utf-8">
<title>QuillBarn23' — Shop</title>
<link href="https://fonts.googleapis.com/css2?family=Oswald:wght@400;500;600&family=Roboto:wght@300;400;500;700&display=swap" rel="stylesheet">
<style>
:root{
  --sky:#7dd0e2;
  --sky-dark:#5fbfd4;
  --pink:#d7a4cf;
  --pink-deep:#c98bc0;
  --ink:#333333;
  --ink-soft:#777777;
  --dark:#2f2f2f;
  --footer:#f5f5f5;
  --white:#ffffff;
  --line:#dddddd;
  --star:#f2a23a;
  --green:#6fd49a;
  --rose:#f07c8f;
}
*{box-sizing:border-box;margin:0;padding:0}
html,body{width:1200px;height:2528px;overflow:hidden;background:var(--white);font-family:'Roboto',sans-serif;color:var(--ink)}
.page{position:relative;width:1200px;height:2528px}
.abs{position:absolute}

/* hero */
.hero-photo{left:0;top:0;width:1200px;height:606px;background:linear-gradient(100deg,#6b4a33 0%,#3c5a7a 22%,#9a3a3a 34%,#7a6a4a 46%,#d9cfc6 62%,#e8e0d8 100%)}
.topbar{left:162px;top:0;width:876px;height:24px;background:var(--sky);color:var(--white);font-size:11px;display:flex;align-items:center;padding:0 18px;gap:28px}
.topbar .right{margin-left:auto;display:flex;gap:16px}
.header{left:162px;top:24px;width:876px;height:124px;background:var(--white);box-shadow:0 2px 6px rgba(0,0,0,.15)}
.logo{position:absolute;left:20px;top:18px;font-family:'Oswald',sans-serif;font-size:26px;font-weight:500;color:var(--ink)}
.logo-dot{display:inline-block;width:10px;height:10px;background:var(--pink);border-radius:50%;margin-left:6px;vertical-align:middle}
.search-label{position:absolute;left:194px;top:42px;font-size:10px;font-weight:500}
.search{position:absolute;left:248px;top:30px;width:352px;height:36px;border:1px solid var(--pink);display:flex}
.search .cat{width:44px;border-right:1px solid var(--line);font-size:11px;display:flex;align-items:center;justify-content:center}
.search .btn{margin-left:auto;width:38px;background:var(--pink);display:flex;align-items:center;justify-content:center}
.help{position:absolute;left:638px;top:30px;display:flex;gap:10px;align-items:center}
.help .circle{width:34px;height:34px;border:2px solid var(--ink);border-radius:50%;display:flex;align-items:center;justify-content:center}
.help .txt{font-size:12px;font-style:italic;font-weight:500}
.help .num{font-family:'Oswald',sans-serif;font-size:19px;color:var(--sky-dark);font-style:normal}
.cart{position:absolute;left:816px;top:36px}
.nav{position:absolute;left:0;top:86px;width:100%;height:38px;border-top:1px solid #eee;display:flex;align-items:center;padding:0 20px;gap:30px;font-size:11px;text-transform:uppercase}
.nav .active{color:var(--sky-dark)}
.nav .offer{margin-left:auto;display:flex;gap:6px;align-items:center}
.nav .offer i{display:inline-block;width:22px;height:12px;background:var(--pink);border-radius:2px}
.hero-copy{left:640px;top:248px;width:420px;text-align:center}
.hero-copy .kick{font-family:'Oswald',sans-serif;font-size:25px;font-weight:400;color:#444;line-height:1.2}
.hero-copy h1{font-family:'Oswald',sans-serif;font-size:40px;font-weight:600;color:#3b3b3b;line-height:1.05;margin-top:0}
.hero-copy .off{font-family:'Oswald',sans-serif;font-size:32px;font-weight:500;color:#3b3b3b;line-height:1.1;margin-top:4px}
.hero-btns{left:746px;top:391px;display:flex;gap:11px}
.hero-btns span{height:32px;display:flex;align-items:center;justify-content:center;font-size:10px;text-transform:uppercase}
.btn-outline{width:102px;border:2px solid #444;color:#333}
.btn-solid{width:103px;background:#3b3b3b;color:var(--white)}

/* features */
.features{left:162px;top:632px;width:878px;display:flex;justify-content:space-between}
.feature{width:202px;height:59px;background:var(--sky);color:var(--white);display:flex;align-items:center;padding:0 10px;gap:10px}
.feature b{display:block;font-size:11px;font-weight:500;text-transform:uppercase}
.feature small{font-size:9px}

/* categories */
.tile{overflow:hidden}
.tile .photo{width:100%;height:100%}
.tile .cap{position:absolute;left:0;bottom:0;width:100%;height:46px;background:rgba(40,40,40,.85);color:var(--white);font-size:22px;font-weight:300;display:flex;align-items:center;justify-content:center}

/* new arrival */
.band-title{left:0;top:1173px;width:1200px;height:76px;background:var(--pink);color:var(--white);font-size:32px;font-weight:700;display:flex;align-items:center;justify-content:center}
.slide .label{position:absolute;left:0;width:100%;top:258px;text-align:center;color:var(--white)}
.slide .label small{display:block;font-size:16px;text-transform:uppercase}
.slide .label strong{font-size:30px;font-weight:700;text-transform:uppercase}
.arrow{width:38px;height:38px;border:2px solid var(--white);border-radius:50%;background:rgba(0,0,0,.35);display:flex;align-items:center;justify-content:center}

/* best selling */
.tabs{left:162px;top:1645px;display:flex}
.tabs span{height:32px;padding:0 14px;display:flex;align-items:center;font-size:14px}
.tab-active{background:var(--white);border:1px solid var(--line);border-bottom:none;color:#333}
.tab-pink{background:var(--pink);color:var(--white)}
.tab-sky{background:var(--sky);color:var(--white)}
.products-box{left:162px;top:1677px;width:878px;height:408px;border:2px solid #ead2e6;border-radius:4px;box-shadow:0 1px 6px rgba(0,0,0,.08)}
.best-title{left:186px;top:1700px;font-size:22px;font-weight:500;color:var(--pink-deep)}
.pager{left:980px;top:1708px;display:flex;gap:4px}
.pager i{width:18px;height:18px;border-radius:50%;background:var(--pink)}
.product{width:190px;text-align:center}
.product .photo{height:205px;border:1px solid var(--line);position:relative}
.product .acts{position:absolute;right:2px;top:64px;display:flex;flex-direction:column;gap:7px}
.product .acts i{width:22px;height:18px;border-radius:3px}
.product .name{margin-top:12px;font-size:13px;white-space:nowrap;margin-left:-10px;margin-right:-10px}
.stars{margin-top:4px;font-size:13px;letter-spacing:1px;color:#bbb}
.stars b{color:var(--star);font-weight:400}
.price{font-size:22px;font-weight:500;margin-top:2px}
.shop{margin:6px auto 0;width:84px;height:27px;background:#2e2e2e;color:var(--white);font-size:10px;display:flex;align-items:center;justify-content:center;text-transform:uppercase}

/* newsletter */
.newsletter{left:0;top:2153px;width:1200px;height:76px;background:var(--sky)}
.newsletter h2{position:absolute;left:162px;top:20px;font-family:'Oswald',sans-serif;font-size:24px;font-weight:500;color:var(--white);text-transform:uppercase}
.field{position:absolute;top:24px;width:242px;height:34px;border:1px solid var(--white);color:var(--white);font-size:11px;padding:0 10px;display:flex;align-items:center}
.submit{position:absolute;left:934px;top:24px;width:102px;height:34px;background:#2e2e2e;color:var(--white);font-size:14px;font-weight:700;display:flex;align-items:center;justify-content:center;gap:4px}

/* footer */
.footer{left:0;top:2229px;width:1200px;height:243px;background:var(--footer)}
.foot-logo{position:absolute;left:160px;top:32px;font-family:'Oswald',sans-serif;font-size:30px;font-weight:500;color:var(--ink)}
.foot-about{position:absolute;left:161px;top:124px;width:215px;font-size:11px;line-height:1.55;color:var(--ink-soft)}
.col{position:absolute;top:40px}
.col h3{font-size:15px;font-weight:500;text-transform:uppercase;margin-bottom:16px;color:#444}
.col li{list-style:none;font-size:11px;color:var(--ink-soft);margin-bottom:10px;text-transform:uppercase}
.col li::before{content:"›";margin-right:6px}
.contact p{display:flex;gap:12px;font-size:11px;color:var(--ink-soft);margin-bottom:16px;line-height:1.5}
.bottombar{left:0;top:2472px;width:1200px;height:56px;background:var(--dark);border-top:3px dashed var(--sky)}
.bottombar .copy{position:absolute;left:160px;top:20px;font-size:11px;color:#ccc}
.cards{position:absolute;left:577px;top:16px;display:flex;gap:5px}
.cards i{width:28px;height:18px;background:#e8e8e8;border-radius:2px}
.social{position:absolute;left:928px;top:14px;display:flex;gap:8px}
.social i{width:22px;height:22px;border:1px solid #aaa;border-radius:50%}
</style>
</head>
<body>
<div class="page">

  <div class="abs hero-photo" role="img" aria-label="Stack of folded coloured fabrics with a tape measure and thread spools on a table"></div>

  <div class="abs topbar">
    <span>Wish list (0)</span><span>My account ▾</span><span>Shopping cart</span><span>Checkout</span>
    <span class="right"><span>USD ▾</span><span>English ▾</span></span>
  </div>

  <header class="abs header">
    <div class="logo">QuillBarn23'<span class="logo-dot"></span></div>
    <div class="search-label">SEARCH</div>
    <div class="search">
      <div class="cat">All ▾</div>
      <div class="btn"><svg width="16" height="16" viewBox="0 0 16 16"><circle cx="6.5" cy="6.5" r="5" fill="none" stroke="#fff" stroke-width="2"/><line x1="10" y1="10" x2="15" y2="15" stroke="#fff" stroke-width="2"/></svg></div>
    </div>
    <div class="help">
      <div class="circle"><svg width="16" height="16" viewBox="0 0 16 16"><rect x="3" y="1" width="10" height="14" rx="2" fill="none" stroke="#333" stroke-width="1.6"/><line x1="6" y1="12" x2="10" y2="12" stroke="#333" stroke-width="1.4"/></svg></div>
      <div class="txt">Need help from us?<br><span class="num">000-000-0000</span></div>
    </div>
    <div class="cart"><svg width="30" height="24" viewBox="0 0 30 24"><path d="M2 3h4l3 12h13l3-9H8" fill="none" stroke="#333" stroke-width="1.8"/><circle cx="11" cy="20" r="2" fill="#333"/><circle cx="20" cy="20" r="2" fill="#333"/><circle cx="24" cy="4" r="4" fill="#d7a4cf"/></svg></div>
    <nav class="nav">
      <span class="active">Home</span><span>About us</span><span>Collection</span><span>Our products</span><span>Shop</span><span>Contact us</span>
      <span class="offer"><i></i>Special offer!</span>
    </nav>
  </header>

  <div class="abs hero-copy">
    <div class="kick">NEW ARRIVALS</div>
    <h1>QUILLBARN23' CLOTHING</h1>
    <div class="off">30%OFF</div>
  </div>
  <div class="abs hero-btns"><span class="btn-outline">New arrivals</span><span class="btn-solid">Shop now</span></div>

  <section class="abs features">
    <div class="feature"><svg width="30" height="22" viewBox="0 0 30 22"><path d="M2 4h16v11H2zM18 8h6l4 4v3h-10z" fill="none" stroke="#fff" stroke-width="1.6"/><circle cx="7" cy="17" r="2.5" fill="#7dd0e2" stroke="#fff" stroke-width="1.6"/><circle cx="23" cy="17" r="2.5" fill="#7dd0e2" stroke="#fff" stroke-width="1.6"/></svg><div><b>Fast delivery</b><small>We provide you with fast and free</small></div></div>
    <div class="feature"><svg width="22" height="26" viewBox="0 0 22 26"><rect x="5" y="2" width="12" height="22" rx="2" fill="none" stroke="#fff" stroke-width="1.6"/></svg><div><b>24/7 Customer service</b><small>We Provide you 24X7 Service</small></div></div>
    <div class="feature"><svg width="28" height="24" viewBox="0 0 28 24"><path d="M2 18c6-4 10 2 16-2l8-6" fill="none" stroke="#fff" stroke-width="1.6"/><circle cx="16" cy="7" r="4" fill="none" stroke="#fff" stroke-width="1.6"/></svg><div><b>30 Day money back</b><small>You can return or exchange</small></div></div>
    <div class="feature"><svg width="26" height="26" viewBox="0 0 26 26"><circle cx="13" cy="13" r="10" fill="none" stroke="#fff" stroke-width="1.6" stroke-dasharray="3 2"/><circle cx="13" cy="13" r="5" fill="none" stroke="#fff" stroke-width="1.6"/></svg><div><b>100% Satisfaction</b><small>You Won't Be Alone</small></div></div>
  </section>

  <div class="abs tile" style="left:162px;top:720px;width:433px;height:414px">
    <div class="photo" role="img" aria-label="Tailored suit jacket on a mannequin in a tailor shop" style="background:linear-gradient(120deg,#5a4a3e,#2a2a2c 55%,#c9c4bd)"></div>
    <div class="cap">Custom Clothing</div>
  </div>
  <div class="abs tile" style="left:612px;top:720px;width:195px;height:202px">
    <div class="photo" role="img" aria-label="Printed white t-shirt lying on wooden boards" style="background:linear-gradient(160deg,#6b4e3a,#e8e6e2 50%,#2a3550)"></div>
    <div class="cap">T-shirts</div>
  </div>
  <div class="abs tile" style="left:612px;top:934px;width:195px;height:200px">
    <div class="photo" role="img" aria-label="Stack of folded sweaters in red, teal and blue" style="background:linear-gradient(180deg,#e86a5a,#3fb3a8 50%,#2f6fb0)"></div>
    <div class="cap">Sweaters</div>
  </div>
  <div class="abs tile" style="left:824px;top:720px;width:214px;height:414px">
    <div class="photo" role="img" aria-label="Woman wearing a grey wide-brim hat and a knit sweater" style="background:linear-gradient(180deg,#8a7f78,#c7bdb6 45%,#a9a6a3)"></div>
    <div class="cap">Hats</div>
  </div>

  <div class="abs band-title">NEW ARRIVAL</div>
  <div class="abs" role="img" aria-label="Rack of coloured coats" style="left:0;top:1249px;width:110px;height:343px;background:linear-gradient(180deg,#7b3a3a,#5a6a3a)"></div>
  <div class="abs slide" style="left:110px;top:1249px;width:493px;height:343px">
    <div role="img" aria-label="Four women modelling winter coats" style="width:100%;height:100%;background:linear-gradient(90deg,#b8b4ae,#4c4a3c 25%,#6b4e3e 45%,#a07a58 65%,#c9c7c4 85%,#d8d6d2)"></div>
    <div class="label"><small>Lorem Ipsum</small><strong>Simply Dummy</strong></div>
  </div>
  <div class="abs slide" style="left:603px;top:1249px;width:479px;height:343px">
    <div role="img" aria-label="Friends in winter hats and jackets laughing outdoors" style="width:100%;height:100%;background:linear-gradient(90deg,#c8b6a6,#a08a78 30%,#2d3442 60%,#9b9ba0)"></div>
    <div class="label"><small>Lorem Ipsum</small><strong>Simply Dummy</strong></div>
  </div>
  <div class="abs" role="img" aria-label="Children in colourful winter clothes" style="left:1082px;top:1249px;width:118px;height:343px;background:linear-gradient(180deg,#a05a4a,#3a6a4a)"></div>
  <div class="abs arrow" style="left:14px;top:1398px"><svg width="16" height="12" viewBox="0 0 16 12"><path d="M15 6H2M6 1L1 6l5 5" fill="none" stroke="#fff" stroke-width="2"/></svg></div>
  <div class="abs arrow" style="left:1140px;top:1398px"><svg width="16" height="12" viewBox="0 0 16 12"><path d="M1 6h13M10 1l5 5-5 5" fill="none" stroke="#fff" stroke-width="2"/></svg></div>

  <div class="abs products-box"></div>
  <div class="abs tabs"><span class="tab-active">Most Popular</span><span class="tab-pink">Top Rated</span><span class="tab-sky">Latest Items</span></div>
  <div class="abs best-title">BEST SELLING:</div>
  <div class="abs pager"><i></i><i></i></div>

  <div class="abs product" style="left:187px;top:1741px">
    <div class="photo" role="img" aria-label="Black leggings" style="background:linear-gradient(180deg,#f2f2f2,#1f2230 40%,#eeeeee)"><div class="acts"><i style="background:var(--sky)"></i><i style="background:var(--green)"></i><i style="background:var(--rose)"></i></div></div>
    <div class="name">Lorem Ipsum is simply dummy</div><div class="stars"><b>★★★</b>★★</div><div class="price">$80.00</div><div class="shop">Shop now</div>
  </div>
  <div class="abs product" style="left:403px;top:1741px">
    <div class="photo" role="img" aria-label="Orange baseball cap with a patch" style="background:radial-gradient(circle at 50% 45%,#d08a3e 35%,#f0f0f0 60%)"><div class="acts"><i style="background:var(--sky)"></i><i style="background:var(--green)"></i><i style="background:var(--rose)"></i></div></div>
    <div class="name">Lorem Ipsum is simply dummy</div><div class="stars"><b>★★★</b>★★</div><div class="price">$99.00</div><div class="shop">Shop now</div>
  </div>
  <div class="abs product" style="left:615px;top:1741px">
    <div class="photo" role="img" aria-label="Black hoodie with a round print" style="background:radial-gradient(circle at 50% 50%,#1e1e1e 45%,#f0f0f0 70%)"><div class="acts"><i style="background:var(--sky)"></i><i style="background:var(--green)"></i><i style="background:var(--rose)"></i></div></div>
    <div class="name">Lorem Ipsum is simply dummy</div><div class="stars"><b>★★★</b>★★</div><div class="price">$78.00</div><div class="shop">Shop now</div>
  </div>
  <div class="abs product" style="left:829px;top:1741px">
    <div class="photo" role="img" aria-label="Red festive knit sweater" style="background:radial-gradient(circle at 50% 50%,#c0282e 40%,#efe6da 48%,#f3f3f3 70%)"><div class="acts"><i style="background:var(--sky)"></i><i style="background:var(--green)"></i><i style="background:var(--rose)"></i></div></div>
    <div class="name">Lorem Ipsum is simply dummy</div><div class="stars"><b>★★★</b>★★</div><div class="price">$69.00</div><div class="shop">Shop now</div>
  </div>

  <section class="abs newsletter">
    <h2>Sign up for newslleter</h2>
    <div class="field" style="left:433px">Enter your name</div>
    <div class="field" style="left:683px">Enter your email</div>
    <div class="submit">SUBMIT <svg width="12" height="12" viewBox="0 0 12 12"><circle cx="6" cy="6" r="5" fill="none" stroke="#fff" stroke-width="1.4"/><path d="M5 3.5L7.5 6 5 8.5" fill="none" stroke="#fff" stroke-width="1.4"/></svg></div>
  </section>

  <footer class="abs footer">
    <div class="foot-logo">QuillBarn23'</div>
    <p class="foot-about">Lorem Ipsum is simply dummy text the printing and typesetting industry. Lorem Ipsum has been the industry's standard and scrambled it to make men book.</p>
    <div class="col" style="left:444px"><h3>Quick links</h3><ul><li>Home</li><li>About us</li><li>Collection</li><li>Our products</li><li>Shop</li></ul></div>
    <div class="col" style="left:652px"><h3>Products</h3><ul><li>T-shirts</li><li>Sweaters</li><li>Hoodies</li><li>Hats</li><li>Leggings</li></ul></div>
    <div class="col contact" style="left:860px"><h3>Contact information</h3>
      <p><svg width="10" height="14" viewBox="0 0 10 14"><path d="M5 13S1 8 1 5a4 4 0 018 0c0 3-4 8-4 8z" fill="#888"/><circle cx="5" cy="5" r="1.5" fill="#f5f5f5"/></svg><span>Lindenweg 48,<br>4812 KR Maplestad, Nederland</span></p>
      <p><svg width="12" height="10" viewBox="0 0 12 10"><rect x="0.5" y="0.5" width="11" height="9" fill="none" stroke="#888"/><path d="M1 1l5 4 5-4" fill="none" stroke="#888"/></svg><span>hello@quillbarn7823.com</span></p>
      <p><svg width="12" height="12" viewBox="0 0 12 12"><path d="M2 1l2.5 0 1 3-1.5 1a7 7 0 003 3l1-1.5 3 1V11C5 11 1 7 1 2z" fill="#888"/></svg><span>000-555-0142</span></p>
    </div>
  </footer>

  <div class="abs bottombar">
    <div class="copy">© 2018 quillbarn7823.com.All Rights Reserved</div>
    <div class="cards"><i></i><i></i><i></i><i></i></div>
    <div class="social"><i></i><i></i><i></i><i></i></div>
  </div>

</div>
</body>
</html>
```